Flyer Design for Maplecrest Suite Residences

We are seeking a skilled and creative designer to create a visually appealing and informative flyer for Maplecrest Suite Residences (MSR). This flyer will be distributed to condo owners in Toronto, introducing our comprehensive management services for their properties. The primary goal of the flyer is to attract condo owners to avail our services and highlight the benefits of partnering with Maplecrest Suite Residences for their property management needs.
Size: 8.5 x 11 inches - single sided
Scope of the Project:
- Design Concept: Develop a visually striking and professional design concept that aligns with Maplecrest Suite Residences' brand identity. The design should be modern, clean, and convey a sense of reliability and expertise in property management.
- Layout and Content: Create an engaging layout that effectively communicates the key features and benefits of our management services. The content should be concise, informative, and persuasive. The following points should be included:
a. Service Offering: Clearly state that Maplecrest Suite Residences specializes in property management services for condo owners in Toronto.
b. Fee Structure: Highlight our competitive pricing model, which includes a management fee of 15% plus tax of the pure rent we manage to secure for the property.
c. Rental Marketing: Emphasize our comprehensive approach to rental marketing by showcasing that we list the unit on our own website, as well as other booking engines such as Stayvio, HOMZ, and other similar platforms (not limited to these).
d. Target Market: Emphasize that Maplecrest Suite Residences specializes in securing one-month minimum executive rentals. However, highlight that we also manage units with short-term rental (STR) permits and can effectively market their properties for durations shorter than one month.
- Visual Elements: Incorporate high-quality images of stylish and well-maintained apartments to visually represent the type of properties we manage. The images should be appealing and complement the overall design.
- Contact Information: Clearly display our contact information, including phone number, email address, and website URL, to encourage interested condo owners to reach out to us.
- Design Variations: Provide the flyer design in multiple file formats (e.g., PDF, JPEG, PNG) to accommodate both digital distribution and printing purposes.
Additional Guidelines:
- Maintain consistency with Maplecrest Suite Residences' brand colors and logo, ensuring a cohesive visual identity.
- Ensure that the design is easy to read and understand, using legible fonts and appropriate font sizes.
- Make effective use of white space and other design elements to create an aesthetically pleasing layout.
- Proofread the content for accuracy, grammar, and spelling errors.
Feel free to contact us if you have any questions or require further clarification during the design process. We appreciate your attention to detail and creativity in helping us create an impactful flyer for Maplecrest Suite Residences.
Thank you for your interest, and we look forward to reviewing your design proposal!
PS: attached is our company logo.
Here's a small inspiration that you can use:
Section 1: Introduction
Discover stress-free property management solutions for your furnished properties in Toronto.
Section 2: Full Management Services
Leave the Hassle to Us!
At Maplecrest Suite Residences, we offer comprehensive full management services for your furnished properties. Our dedicated team takes care of all the details, ensuring a seamless and hands-free experience for you and your guests.
Section 3: Why Choose Maplecrest Suite Residences?
Experience the Benefits:
1. Time and Convenience: We handle all aspects of property management, from tenant screening and lease agreements to maintenance requests and rent collection. Relax and let us take care of it all!
2. Maximizing Returns: Our team is committed to maximizing your rental income, while minimizing vacancies. We use strategic marketing techniques to attract qualified tenants and optimize rental rates.
3. Industry Connections: Benefit from our extensive network of industry professionals. We collaborate with photographers, cleaners, and maintenance providers to ensure your property always looks its best with minimum costs.
Section 4: Our Approach
Customized Solutions for Your Property:
1. Property Marketing: We leverage our expertise to market your property effectively. We list your unit on our own website (maplecrestsuiteresidences-demo.com) and other popular booking platforms, attracting a wide range of potential tenants.
2. Tenant Screening: Our rigorous tenant screening process ensures that only qualified and reliable individuals occupy your property. Your peace of mind is our priority.
3. Rental Management: From managing inquiries and scheduling viewings to handling lease agreements and rent collection, we oversee every aspect of the rental process.
Section 5: Contact Us
Ready to Partner with Us?
Experience the benefits of stress-free property management. Contact Maplecrest Suite Residences today to learn more about our full management services for furnished properties in Toronto.
Phone: [Insert Phone Number] Email: [Insert Email Address] Website: [Insert Website URL] QR Code: [Insert QR Code]
Make the 15% plus tax management fee obvious
Property Management and Executive Rentals

```html
<!DOCTYPE html>
<html lang="en">
<head>
<meta charset="utf-8">
<title>Maplecrest Suite Residences – Property Management Flyer</title>
<link rel="stylesheet" href="https://fonts.googleapis.com/css2?family=Fira+Sans:wght@500;600;700&display=swap">
<style>
  :root {
    --teal-band: #4a9a94;
    --brand-blue: #1d6f96;
    --heading-teal: #1e6a80;
    --label-ink: #1f5f75;
    --paper: #ffffff;
    --interior-light: #f6f4f0;
    --interior-mid: #e4d8c8;
    --wood: #c98a55;
    --sunset: #f5a733;
  }
  * { margin: 0; padding: 0; box-sizing: border-box; }
  html, body { width: 848px; height: 1200px; overflow: hidden; background: var(--paper); }
  body { font-family: "Fira Sans", Arial, sans-serif; }

  .flyer { position: relative; width: 848px; height: 1200px; overflow: hidden; }

  .interior-photo {
    position: absolute; inset: 0;
    background:
      radial-gradient(ellipse 420px 560px at 760px 260px, rgba(255,255,255,0.95) 0%, rgba(255,255,255,0.6) 45%, rgba(255,255,255,0) 100%),
      radial-gradient(ellipse 360px 220px at 560px 720px, rgba(201,138,85,0.35) 0%, rgba(201,138,85,0) 100%),
      linear-gradient(120deg, rgba(201,138,85,0) 55%, rgba(201,138,85,0.18) 70%, rgba(201,138,85,0) 85%),
      linear-gradient(180deg, var(--interior-light) 0%, #eee8df 38%, var(--interior-mid) 62%, #f2cd8c 80%, var(--sunset) 96%);
  }
  .top-band { position: absolute; left: 54px; top: 0; width: 740px; height: 31px; background: var(--teal-band); }

  .graphics { position: absolute; inset: 0; }

  .brand-box {
    position: absolute; left: 50px; top: 88px; width: 216px; height: 215px;
    background: var(--paper); border: 2px solid var(--brand-blue);
    display: flex; flex-direction: column; align-items: center; justify-content: center; gap: 14px;
  }
  .brand-box .brand-square { width: 44px; height: 44px; background: var(--teal-band); }
  .brand-box .brand-name {
    color: var(--teal-band); font-weight: 600; font-size: 15px; letter-spacing: 1.5px;
    text-align: center; line-height: 1.3; text-transform: uppercase;
  }

  .headline {
    position: absolute; left: 300px; top: 84px; width: 430px;
    color: var(--heading-teal); font-weight: 600; font-size: 38px; line-height: 1.12;
  }

  .fee-word {
    position: absolute; left: 84px; top: 405px; width: 76px; text-align: center;
    color: var(--brand-blue); font-weight: 700; font-size: 27px;
  }

  .tag {
    position: absolute; display: flex; align-items: center; padding-left: 28px;
    background: var(--paper); color: var(--label-ink); font-weight: 600; font-size: 27px; line-height: 1.15;
    clip-path: polygon(0 0, 88% 0, 100% 50%, 88% 100%, 0 100%);
  }
  .tag--hex { justify-content: center; padding-left: 0; clip-path: polygon(14% 0, 86% 0, 100% 50%, 86% 100%, 14% 100%, 0 50%); font-size: 30px; }
  .tag.fee-rate { left: 275px; top: 382px; width: 127px; height: 88px; }
  .tag.own-site { left: 292px; top: 570px; width: 207px; height: 85px; }
  .tag.platforms { left: 292px; top: 662px; width: 207px; height: 86px; }
  .tag.one-month { left: 292px; top: 805px; width: 207px; height: 64px; }
  .tag.str { left: 292px; top: 890px; width: 207px; height: 93px; }

  .contact {
    position: absolute; left: 236px; top: 1088px; display: flex; align-items: center; gap: 20px;
    color: var(--heading-teal); font-weight: 600; font-size: 29px;
  }
</style>
</head>
<body>
<main class="flyer">
  <div class="interior-photo" role="img" aria-label="Bright furnished condo interior with dining table, white chairs, rug and open wooden staircase by tall windows"></div>
  <div class="top-band"></div>

  <svg class="graphics" width="848" height="1200" viewBox="0 0 848 1200">
    <path class="skyline-area" role="img" aria-label="White Toronto skyline silhouette rising toward the right" fill="#ffffff"
          d="M0,1200 V1168 H150 C150,1100 170,1062 230,1062 C480,1062 690,990 848,790 V1200 Z"/>

    <g class="case case--small" aria-hidden="true">
      <path d="M330,258 v-12 h30 v12" fill="none" stroke="var(--brand-blue)" stroke-width="5"/>
      <rect x="303" y="257" width="82" height="46" rx="5" fill="var(--brand-blue)"/>
      <path d="M332,283 l12,-10 l12,10 v14 h-24 z" fill="#fff"/>
      <rect x="340" y="287" width="7" height="10" fill="var(--brand-blue)"/>
    </g>

    <g class="case case--fee" aria-hidden="true">
      <path d="M112,372 v-18 h80 v18" fill="none" stroke="var(--brand-blue)" stroke-width="7"/>
      <rect x="64" y="370" width="171" height="103" rx="8" fill="var(--brand-blue)"/>
      <circle cx="122" cy="422" r="42" fill="#fff"/>
      <line x1="164" y1="422" x2="275" y2="426" stroke="#fff" stroke-width="3"/>
      <circle cx="164" cy="422" r="5" fill="#fff"/>
    </g>

    <g class="case case--marketing" aria-hidden="true">
      <path d="M105,565 v-18 h70 v18" fill="none" stroke="var(--brand-blue)" stroke-width="7"/>
      <rect x="64" y="563" width="150" height="95" rx="8" fill="var(--brand-blue)"/>
      <g fill="none" stroke="#fff" stroke-width="4">
        <circle cx="139" cy="611" r="30"/>
        <ellipse cx="139" cy="611" rx="13" ry="30"/>
        <line x1="109" y1="611" x2="169" y2="611"/>
        <line x1="139" y1="581" x2="139" y2="641"/>
      </g>
      <g stroke="#fff" stroke-width="3" fill="#fff">
        <line x1="169" y1="625" x2="292" y2="613"/>
        <line x1="169" y1="625" x2="292" y2="705"/>
        <circle cx="169" cy="625" r="5"/>
      </g>
    </g>

    <g class="case case--rental" aria-hidden="true">
      <path d="M105,793 v-18 h70 v18" fill="none" stroke="var(--brand-blue)" stroke-width="7"/>
      <rect x="64" y="791" width="150" height="95" rx="8" fill="var(--brand-blue)"/>
      <path d="M160,815 a30,30 0 1 0 10,30" fill="none" stroke="#fff" stroke-width="7"/>
      <path d="M154,802 l16,14 l-19,6 z" fill="#fff"/>
      <path d="M122,839 l17,-15 l17,15 v18 h-34 z" fill="#fff"/>
      <rect x="134" y="843" width="9" height="14" fill="var(--brand-blue)"/>
      <g stroke="#fff" stroke-width="3" fill="#fff">
        <line x1="170" y1="838" x2="292" y2="837"/>
        <line x1="170" y1="838" x2="292" y2="935"/>
        <circle cx="170" cy="838" r="5"/>
      </g>
    </g>
  </svg>

  <div class="brand-box">
    <span class="brand-square"></span>
    <span class="brand-name">Maplecrest Suite<br>Residences</span>
  </div>

  <h1 class="headline">Property management services for condo owners in Toronto.</h1>

  <span class="fee-word">Fee</span>
  <div class="tag tag--hex fee-rate">15%</div>
  <div class="tag own-site">Own<br>website</div>
  <div class="tag platforms">Stayvio,<br>HOMZ, others</div>
  <div class="tag one-month">One-month</div>
  <div class="tag str">Short-term<br>rental (STR)</div>

  <div class="contact">
    <svg width="58" height="52" viewBox="0 0 58 52" aria-hidden="true">
      <path d="M30,4 a22,22 0 1 1 -14,39 l-12,5 l5,-12 a22,22 0 0 1 21,-32 z" fill="none" stroke="var(--heading-teal)" stroke-width="5"/>
      <circle cx="8" cy="14" r="3.5" fill="var(--heading-teal)"/>
      <circle cx="18" cy="14" r="3.5" fill="var(--heading-teal)"/>
      <circle cx="28" cy="14" r="3.5" fill="var(--heading-teal)"/>
    </svg>
    <span>Contact info</span>
  </div>
</main>
</body>
</html>
```